Etiketten für Honig
Zielgruppe
Es scheint Missverständnisse zu geben weshalb ich das Briefing wohl ändern muss.
see below for English translation
Wir sind eine kleine Imkerei, die von der Liebhaberei in den Nebenerwerb wechselt. Wir verkaufen verschiedene Sortenhonige und Honigzubereitungen (siehe Webseite) im vorwiegend ländlichen Raum des Münsterlandes.
Entsprechend unseres Standortes und unserer Kundschaft benötigen wir ein klassisch ländliches Design. Hierfür haben wir auch bereits ein Logo welches verwendet werden muss.
English
There seems to be some misunderstanding, so I guess I'll have to change the briefing.
We are a small apiary that changes from hobby to sideline. We sell different types of honey and honey preparations (e.g. honey with raspberry) in a predominantly rural area of the Münsterland (Muensterland).
According to our location and our clientele, we need a classic rural design. We already have a logo which must be used.
Aufgabenstellung
Wir möchten ein rechteckiges Etikett mit Gewährverschluss das für verschiedene Sorten adoptierbar ist. Zum Beispiel durch den Austausch der Sortenbezeichnung und eine farbliche Veränderung.
Das Design soll später auf Naturpapier oder Graspapier gedruckt werden. Das Logo muss auf Etikett und Gewährverschluss abgebildet werden.
We would like a rectangular label with a guarantee seal that is adoptable for different varieties. For example, by exchanging the variety designation and changing the color.
The design will later be printed on uncoated paper or grass paper. The logo must be shown on the label and guarantee seal.

```html
<!DOCTYPE html>
<html lang="de">
<head>
<meta charset="utf-8">
<title>Honigetiketten – Frühtracht und Blütenhonig</title>
<link rel="stylesheet" href="https://fonts.googleapis.com/css2?family=Herr+Von+Muellerhoff&family=Raleway:ital,wght@0,400;0,500;1,500&display=swap">
<style>
  :root {
    --backdrop: #5a5a5a;
    --paper: #efece2;
    --ink: #555550;
    --seam: #9a9a96;
    --spring: #dbd733;
    --blossom: #f28f4a;
  }
  * { box-sizing: border-box; margin: 0; padding: 0; }
  html, body { width: 1200px; height: 1200px; overflow: hidden; }
  body { background: var(--backdrop); position: relative; font-family: "Raleway", sans-serif; color: var(--ink); }

  .label-set { position: absolute; width: 436px; height: 447px; }
  .label-set--spring { left: 104px; top: 376px; --accent: var(--spring); }
  .label-set--blossom { left: 630px; top: 371px; --accent: var(--blossom); }

  .seal-stem { position: absolute; left: 162px; top: 130px; width: 112px; height: 70px; background: var(--paper); }
  .seal { position: absolute; left: 137px; top: 0; width: 162px; height: 162px; border-radius: 50%; background: var(--paper); border: 1px solid #fff; }
  .seal svg { position: absolute; left: 1px; top: 12px; }
  .seal-content { position: absolute; inset: 0; display: flex; flex-direction: column; align-items: center; padding-top: 26px; }
  .seal-brand { display: flex; align-items: center; gap: 3px; font-size: 8px; font-weight: 500; letter-spacing: .3px; }
  .brand-dot { width: 7px; height: 7px; border-radius: 50%; background: var(--ink); }
  .seal-title { font-family: "Herr Von Muellerhoff", cursive; font-size: 33px; line-height: 32px; text-align: center; margin-top: 6px; }

  .label { position: absolute; left: 0; top: 198px; width: 436px; height: 249px; background: var(--paper); border: 1px solid #fff; }
  .comb { position: absolute; top: 0; background: var(--accent); border-radius: 0 0 14px 14px; opacity: .95; }
  .comb--left { left: 62px; width: 55px; height: 55px; }
  .comb--right { left: 321px; width: 79px; height: 58px; }
  .brand { position: absolute; left: 0; right: 0; top: 62px; display: flex; justify-content: center; align-items: center; gap: 8px; font-size: 20px; font-weight: 500; letter-spacing: .5px; }
  .brand .brand-dot { width: 16px; height: 16px; }
  .title { position: absolute; left: 0; right: 0; top: 128px; text-align: center; font-family: "Herr Von Muellerhoff", cursive; font-size: 52px; line-height: 60px; }
  .variety { position: absolute; left: 108px; top: 204px; display: flex; align-items: center; gap: 10px; color: var(--accent); font-size: 23px; font-weight: 400; letter-spacing: .3px; }
  .label-set--blossom .variety { left: 92px; }
  .hex { width: 14px; height: 13px; background: var(--accent); clip-path: polygon(25% 0, 75% 0, 100% 50%, 75% 100%, 25% 100%, 0 50%); }
  .weight { position: absolute; right: 14px; top: 206px; font-size: 18px; font-style: italic; font-weight: 500; }
</style>
</head>
<body>

<section class="label-set label-set--spring">
  <div class="seal-stem"></div>
  <div class="seal">
    <svg width="160" height="138" viewBox="0 0 160 138" aria-hidden="true">
      <polygon points="1,69 40,1 120,1 159,69 120,137 40,137" fill="var(--spring)" stroke="var(--seam)" stroke-width="1" stroke-dasharray="3 2"/>
    </svg>
    <div class="seal-content">
      <div class="seal-brand"><span class="brand-dot"></span>Imkerei Brenner</div>
      <p class="seal-title">Ellerbacher<br>Landhonig</p>
    </div>
  </div>
  <div class="label">
    <div class="comb comb--left" role="img" aria-label="Wabenmuster"></div>
    <div class="comb comb--right" role="img" aria-label="Wabenmuster"></div>
    <div class="brand"><span class="brand-dot"></span>Imkerei Brenner</div>
    <p class="title">Ellerbacher Landhonig</p>
    <p class="variety"><span class="hex"></span>FRÜHTRACHT<span class="hex"></span></p>
    <p class="weight">250g</p>
  </div>
</section>

<section class="label-set label-set--blossom">
  <div class="seal-stem"></div>
  <div class="seal">
    <svg width="160" height="138" viewBox="0 0 160 138" aria-hidden="true">
      <polygon points="1,69 40,1 120,1 159,69 120,137 40,137" fill="var(--blossom)" stroke="var(--seam)" stroke-width="1" stroke-dasharray="3 2"/>
    </svg>
    <div class="seal-content">
      <div class="seal-brand"><span class="brand-dot"></span>Imkerei Brenner</div>
      <p class="seal-title">Ellerbacher<br>Landhonig</p>
    </div>
  </div>
  <div class="label">
    <div class="comb comb--left" role="img" aria-label="Wabenmuster"></div>
    <div class="comb comb--right" role="img" aria-label="Wabenmuster"></div>
    <div class="brand"><span class="brand-dot"></span>Imkerei Brenner</div>
    <p class="title">Ellerbacher Landhonig</p>
    <p class="variety"><span class="hex"></span>BLÜTENHONIG<span class="hex"></span></p>
    <p class="weight">250g</p>
  </div>
</section>

</body>
</html>
```